Business Card Design for Software Development Company

I am looking for a business card design the incorporates my new logo (attached below).

Key information to include:
Name: Marcus Delvine
Title: CEO
Email: marcus@brightwellcivic.com
Phone: 555-218-4093
Website: www.brightwellcivic.com

NOTE: This design should be easy to edit so that we can order cards for different members of our team.

```html
<!DOCTYPE html>
<html lang="en">
<head>
<meta charset="utf-8">
<title>Brightwell Labs – Business Card</title>
<link href="https://fonts.googleapis.com/css2?family=Montserrat:wght@400;500;600&display=swap" rel="stylesheet">
<style>
  :root {
    --backdrop: #9d9d9d;
    --paper: #f4f4f2;
    --ink: #2c3248;
    --ink-soft: #4a5066;
    --accent-teal: #23b3a0;
    --accent-orange: #ef8a2c;
  }
  * { box-sizing: border-box; margin: 0; padding: 0; }
  html, body {
    width: 1200px;
    height: 956px;
    overflow: hidden;
    background: var(--backdrop);
    font-family: "Montserrat", sans-serif;
    color: var(--ink);
  }
  .canvas { position: relative; width: 1200px; height: 956px; }

  .card {
    position: absolute;
    width: 630px;
    height: 360px;
    background: var(--paper);
    box-shadow: 0 18px 40px rgba(0,0,0,0.28);
  }
  .card--front { left: 70px; top: 90px; }
  .card--back  { left: 500px; top: 510px; }

  /* Wordmark */
  .wordmark { position: absolute; }
  .wordmark__row { display: flex; align-items: center; gap: 12px; }
  .wordmark__dot {
    width: 30px; height: 30px; border-radius: 50%;
    background: var(--accent-teal);
  }
  .wordmark__name {
    font-weight: 600;
    color: var(--ink);
    letter-spacing: -0.5px;
    line-height: 1;
  }
  .wordmark__tagline {
    font-size: 6.5px;
    font-weight: 500;
    letter-spacing: 0.8px;
    text-transform: uppercase;
    color: var(--ink);
    text-align: right;
    margin-top: 4px;
  }

  .card--front .wordmark { left: 44px; top: 48px; }
  .card--front .wordmark__name { font-size: 42px; }

  .card--back .wordmark { left: 110px; top: 140px; }
  .card--back .wordmark__name { font-size: 52px; }
  .card--back .wordmark__tagline { font-size: 8px; }

  /* Person */
  .person { position: absolute; left: 44px; top: 150px; }
  .person__name {
    font-size: 22px; font-weight: 500; letter-spacing: 0.5px;
    text-transform: uppercase; color: var(--ink);
  }
  .person__title { font-size: 14px; color: var(--ink-soft); margin-top: 2px; }
  .person__rule { width: 22px; height: 1px; background: var(--ink); margin-top: 14px; }

  .contact { position: absolute; left: 44px; top: 236px; list-style: none; }
  .contact__item {
    display: flex; align-items: center; gap: 10px;
    font-size: 14px; color: var(--ink); margin-bottom: 9px;
  }
  .contact__icon { width: 12px; height: 12px; fill: var(--ink); flex: none; }

  .accent-shape {
    position: absolute; right: 60px; top: 90px;
    width: 190px; height: 190px; border-radius: 50%;
    background: linear-gradient(160deg, var(--accent-teal), var(--accent-orange));
  }
</style>
</head>
<body>
<main class="canvas">

  <section class="card card--front" aria-label="Business card front">
    <div class="wordmark">
      <div class="wordmark__row">
        <span class="wordmark__name">Brightwell Labs</span>
      </div>
      <div class="wordmark__tagline">A division of Brightwell Civic</div>
    </div>

    <div class="person">
      <div class="person__name">Marcus Delvine</div>
      <div class="person__title">CEO</div>
      <div class="person__rule"></div>
    </div>

    <ul class="contact">
      <li class="contact__item">
        <svg class="contact__icon" viewBox="0 0 24 24" aria-hidden="true"><path d="M6.6 10.8a15.1 15.1 0 0 0 6.6 6.6l2.2-2.2c.3-.3.7-.4 1-.2 1.1.4 2.3.6 3.6.6.6 0 1 .4 1 1V20c0 .6-.4 1-1 1A17 17 0 0 1 3 4c0-.6.4-1 1-1h3.5c.6 0 1 .4 1 1 0 1.3.2 2.5.6 3.6.1.3 0 .7-.2 1z"/></svg>
        555-218-4093
      </li>
      <li class="contact__item">
        <svg class="contact__icon" viewBox="0 0 24 24" aria-hidden="true"><path d="M2 5h20v14H2z M2 5l10 8 10-8" fill="none" stroke="currentColor"/><path d="M2 5h20L12 12z M2 7l10 7 10-7v12H2z"/></svg>
        marcus@brightwellcivic.com
      </li>
      <li class="contact__item">
        <svg class="contact__icon" viewBox="0 0 24 24" aria-hidden="true"><path d="M12 2a10 10 0 1 0 0 20 10 10 0 0 0 0-20zm0 2c.9 0 2.2 2 2.7 5H9.3C9.8 6 11.1 4 12 4zM4.3 11h3a17 17 0 0 0 0 2h-3a8 8 0 0 1 0-2zm5 0h5.4a15 15 0 0 1 0 2H9.3a15 15 0 0 1 0-2zm7.4 0h3a8 8 0 0 1 0 2h-3a17 17 0 0 0 0-2zM9.3 15h5.4c-.5 3-1.8 5-2.7 5s-2.2-2-2.7-5z"/></svg>
        www.brightwellcivic.com
      </li>
    </ul>

    <div class="accent-shape" role="img" aria-label="Brand accent shape"></div>
  </section>

  <section class="card card--back" aria-label="Business card back">
    <div class="wordmark">
      <div class="wordmark__row">
        <span class="wordmark__dot" aria-hidden="true"></span>
        <span class="wordmark__name">Brightwell Labs</span>
      </div>
      <div class="wordmark__tagline">A division of Brightwell Civic</div>
    </div>
  </section>

</main>
</body>
</html>
```